Wordpress Design Project

We need a new Wordpress theme for our business Velvora. Velvora specializes in creating custom adult sex toys using CAD and 3D Printing technologies as part of the process. The business's tagline is "Your Pleasure, Your Way".

We are currently using the "Pivot Canvas" theme as a landing page (http://www.velvora.example). We are however we have out grown the single page design and are looking for something new that will allow us to take the next step.

We are looking for something sensual, romantic and sexy, but not something explicit and vulgar.

As the company will be targeting mid to high-end clientele tastefulness is very important to us - this is difficult when the service we are selling is sex but can be achieved.

We would also like for the design to tie in with our current logo and business card designs (Attached).

Target Market(s)

Adults between the ages of 21 and 50 (Predominantly female but not limited to) who like there sex toys and want a custom job.

Industry/Entity Type

Adult

Requirements
Nice to have
• A WordPress design that we particularly like is http://www.tolvane-capital.example/
Should not have
• - Explicit/vulgar illustrations;
- "Clip-Art" should not be used.

```html
<!DOCTYPE html>
<html lang="en">
<head>
<meta charset="utf-8">
<title>Velvora – Your Pleasure, Your Way</title>
<link rel="stylesheet" href="https://fonts.googleapis.com/css2?family=Roboto+Condensed:wght@400;700&family=Roboto:wght@400;500&display=swap">
<style>
  :root {
    --wine: #6a0d10;
    --red: #a30607;
    --red-deep: #8c0405;
    --red-bright: #c4161c;
    --sidebar: #fdf6f6;
    --rule: #d9d0d0;
    --nav-text: #6d6464;
    --accent: #9c0d12;
    --white: #ffffff;
    --button: #8e0a0d;
    --button-dark: #5e0507;
  }
  * { box-sizing: border-box; margin: 0; padding: 0; }
  html, body { width: 1200px; height: 700px; overflow: hidden; }
  body { font-family: "Roboto", Arial, sans-serif; background: var(--red); position: relative; }

  .sidebar { position: absolute; left: 0; top: 0; width: 360px; height: 700px; background: var(--sidebar); }
  .brand-block { height: 175px; background: var(--wine); position: relative; border-bottom: 3px solid #e8dede; }
  .brand-name { position: absolute; left: 125px; top: 55px; font-family: "Roboto", Arial, sans-serif; font-weight: 500; font-size: 44px; color: var(--white); letter-spacing: -0.5px; }
  .brand-tagline { position: absolute; left: 126px; top: 102px; font-size: 16px; color: var(--white); }

  .main-nav { position: absolute; left: 118px; top: 190px; width: 240px; list-style: none; }
  .main-nav li { height: 36px; border-bottom: 1px dashed var(--rule); display: flex; align-items: center; padding-left: 21px; position: relative;
    font-family: "Roboto Condensed", Arial, sans-serif; font-size: 15px; color: var(--nav-text); letter-spacing: 0.3px; }
  .main-nav li::before { content: "›"; position: absolute; left: 0; font-size: 17px; color: #8e8686; top: 7px; }
  .main-nav li.is-current { color: var(--accent); }

  .section-rule { position: absolute; left: 118px; width: 240px; height: 4px; background: linear-gradient(to bottom, #ebe2e2, transparent); border-radius: 2px; }

  .newsletter-title { position: absolute; left: 120px; top: 407px; font-family: "Roboto Condensed", Arial, sans-serif; font-size: 19px; color: var(--accent); }
  .newsletter-input { position: absolute; left: 119px; top: 447px; width: 232px; height: 33px; border: 1px solid #cfc6c6; border-radius: 3px; background: var(--white); }
  .signup-button { position: absolute; left: 280px; top: 489px; width: 71px; height: 32px; background: var(--button); color: var(--white);
    font-family: "Roboto Condensed", Arial, sans-serif; font-size: 16px; display: flex; align-items: center; justify-content: center; border-radius: 2px; box-shadow: 0 1px 2px rgba(0,0,0,.3); }

  .social { position: absolute; top: 565px; left: 0; width: 360px; height: 30px; }
  .social span { position: absolute; width: 30px; height: 30px; border-radius: 50%; background: #ee2a36; }

  .footer-note { position: absolute; left: 137px; top: 649px; font-size: 11px; font-weight: 500; color: #666; letter-spacing: 0.4px; }

  .content { position: absolute; left: 360px; top: 0; width: 840px; height: 700px;
    background: radial-gradient(ellipse at 45% 30%, #b10a0c 0%, var(--red) 55%, var(--red-deep) 100%); }
  .hero-title { position: absolute; left: 0; top: 30px; width: 730px; text-align: center; font-family: "Roboto Condensed", Arial, sans-serif;
    font-size: 22.5px; line-height: 29px; color: var(--white); letter-spacing: 0.2px; }
  .hero-visual { position: absolute; left: 220px; top: 92px; width: 290px; height: 150px; border-radius: 40px;
    background: linear-gradient(to right, #9a9a9a, #c9c9c9 25%, #c7a35a 40%, #1b1b1b 55%, #d6b06a 65%, #bdbdbd 78%, #4a1030 92%); opacity: 0.85; }
  .hero-text { position: absolute; left: 40px; top: 265px; width: 650px; text-align: center; font-family: "Roboto Condensed", Arial, sans-serif;
    font-size: 15.5px; line-height: 21px; color: var(--white); }
  .slider-dots { position: absolute; left: 140px; top: 347px; width: 460px; height: 12px; }
  .slider-dots::before, .slider-dots::after { content: ""; position: absolute; top: 6px; width: 180px; height: 1px; background: linear-gradient(to right, transparent, #7c0305); }
  .slider-dots::before { left: 0; }
  .slider-dots::after { right: 0; transform: scaleX(-1); }
  .slider-dots span { position: absolute; top: 0; width: 12px; height: 12px; border-radius: 50%; background: #3a0202; border: 2px solid #6a6a6a; }
  .slider-dots span.is-active { background: var(--white); border-color: #3a0202; }
  .content-divider { position: absolute; left: 20px; top: 384px; width: 690px; height: 12px;
    background: radial-gradient(ellipse at 50% 0%, rgba(70,0,0,.55), transparent 70%); }

  .product { position: absolute; top: 431px; width: 140px; text-align: center; color: var(--white); }
  .product-visual { width: 140px; height: 130px; border: 1px solid #b51d20;
    background: radial-gradient(ellipse at center, #d21a1e 0%, #9c0507 75%); position: relative; }
  .product-visual::after { content: ""; position: absolute; left: 58px; top: 8px; width: 24px; height: 105px; border-radius: 12px 12px 6px 6px; background: var(--shape, linear-gradient(to right,#777,#ddd,#777)); opacity: .9; }
  .product-name { margin-top: 8px; font-family: "Roboto Condensed", Arial, sans-serif; font-size: 17px; }
  .product-desc { margin-top: 6px; font-size: 11.5px; line-height: 14px; }
  .buy-button { margin: 9px auto 0; width: 110px; height: 34px; background: var(--button); border: 1px solid var(--button-dark);
    font-family: "Roboto Condensed", Arial, sans-serif; font-size: 17px; display: flex; align-items: center; justify-content: center; box-shadow: 0 2px 3px rgba(0,0,0,.3); }
</style>
</head>
<body>
  <aside class="sidebar">
    <header class="brand-block">
      <div class="brand-name">Velvora</div>
      <div class="brand-tagline">your pleasure, your way</div>
    </header>

    <ul class="main-nav">
      <li class="is-current">HOME</li>
      <li>ABOUT</li>
      <li>PRODUCTS</li>
      <li>SHOP</li>
      <li>CONTACT</li>
    </ul>

    <div class="section-rule" style="top:394px"></div>
    <h2 class="newsletter-title">NEWSLETTER SIGN UP</h2>
    <div class="newsletter-input"></div>
    <div class="signup-button">SIGN UP</div>

    <div class="section-rule" style="top:536px"></div>
    <div class="social" aria-label="Social links">
      <span style="left:156px"></span>
      <span style="left:197px"></span>
      <span style="left:241px"></span>
      <span style="left:284px"></span>
    </div>
    <div class="section-rule" style="top:614px"></div>

    <p class="footer-note">© 2013 VELVORA | PRIVACY | TERMS</p>
  </aside>

  <main class="content">
    <h1 class="hero-title">VELVORA IS MAKING IT POSSIBLE FOR YOU TO CREATE TRULY<br>PERSONALISED SEX TOYS IN THE COMFORT OF YOUR OWN HOME.</h1>
    <div class="hero-visual" role="img" aria-label="Row of seven 3D-rendered toy designs in silver, gold, black and plum"></div>
    <p class="hero-text">YOU'LL BE ABLE TO SELECT A TOY DESIGN AND CUSTOMISE IT TO YOUR DESIRE INCLUDING WIDTH, HEIGHT, COLOUR AND MATERIALS. ALL LIVE AND INTERACTIVE ON THE SCREEN IN GLORIOUS 3D. YEP, WE'RE PRETTY EXCITED TOO.</p>
    <div class="slider-dots">
      <span style="left:186px"></span>
      <span class="is-active" style="left:204px"></span>
      <span style="left:222px"></span>
      <span style="left:240px"></span>
    </div>
    <div class="content-divider"></div>

    <article class="product" style="left:25px">
      <div class="product-visual" role="img" aria-label="Silver ribbed toy design render"></div>
      <h3 class="product-name">Velvora</h3>
      <p class="product-desc">You'll be able to select a<br>toy design &amp; customise...</p>
      <div class="buy-button">BUY NOW!</div>
    </article>
    <article class="product" style="left:205px">
      <div class="product-visual" role="img" aria-label="Silver beaded toy design render"></div>
      <h3 class="product-name">Velvora</h3>
      <p class="product-desc">You'll be able to select a<br>toy design &amp; customise...</p>
      <div class="buy-button">BUY NOW!</div>
    </article>
    <article class="product" style="left:385px">
      <div class="product-visual" style="--shape:linear-gradient(to right,#000,#333,#000)" role="img" aria-label="Black tapered toy design render"></div>
      <h3 class="product-name">Velvora</h3>
      <p class="product-desc">You'll be able to select a<br>toy design &amp; customise...</p>
      <div class="buy-button">BUY NOW!</div>
    </article>
    <article class="product" style="left:565px">
      <div class="product-visual" role="img" aria-label="Silver sculpted toy design render"></div>
      <h3 class="product-name">Velvora</h3>
      <p class="product-desc">You'll be able to select a<br>toy design &amp; customise...</p>
      <div class="buy-button">BUY NOW!</div>
    </article>
  </main>
</body>
</html>
```